Hair Extension Aftercare sheet

This sheet is to give to customers regarding the aftercare of hair extensions. There should be Simple and minimal look - approx A5 size and can be folded to suit. I have attached the content and logo files for use.
We are not looking for to much artwork just clean, professional look.
All the content provided in a compact flyer format i.e
A foldable A5 pamphlet or the like, this is for packaging requirements
Please do not submit A4 layouts

Industry/Entity Type

Hair And Beauty

Requirements
Must have
• All the content provided in a compact flyer format i.e
• A foldable A5 pamphlet or the like, this is for packaging requirements
Should not have
• tacky art work or images - must be clean lines

```html
<!DOCTYPE html>
<html lang="en">
<head>
<meta charset="utf-8">
<title>Elena Marlow Hair Extensions – Aftercare Pamphlet</title>
<link href="https://fonts.googleapis.com/css2?family=Cormorant+Garamond:wght@500&family=Open+Sans:wght@400;700&display=swap" rel="stylesheet">
<style>
  :root{
    --bg:#e3e3e3;
    --paper:#f7f7f5;
    --gold:#e6cd8f;
    --gold-deep:#c9a24a;
    --gold-panel:#e3c98c;
    --gold-panel-dark:#d6bb7b;
    --ink:#1e1e1e;
    --text:#4a3d20;
    --alert:#d8243a;
    --dark:#262626;
  }
  *{box-sizing:border-box;margin:0;padding:0}
  html,body{width:1200px;height:1200px;overflow:hidden}
  body{background:var(--bg);position:relative;font-family:"Open Sans",sans-serif}

  /* Brand lockup */
  .brand{display:flex;flex-direction:column;align-items:center;gap:6px;color:var(--gold-deep);font-family:"Cormorant Garamond",serif;font-weight:500;text-align:center}
  .brand-mark{width:14px;height:14px;background:var(--gold-deep)}
  .brand-name{font-size:22px;letter-spacing:2px;line-height:1}
  .brand-sub{font-size:9px;letter-spacing:3px;line-height:1}
  .brand.small .brand-mark{width:5px;height:5px}
  .brand.small{gap:2px}
  .brand.small .brand-name{font-size:7px;letter-spacing:1px}
  .brand.small .brand-sub{font-size:4px;letter-spacing:1px}

  /* Outer pages */
  .sheet{position:absolute;background:var(--paper);box-shadow:0 6px 18px rgba(0,0,0,.12)}
  .band{position:absolute;left:0;right:0;height:38px;background:var(--gold)}
  .band.top{top:0}
  .band.bottom{bottom:0}
  .rule{position:absolute;left:0;right:0;height:5px;background:var(--ink)}
  .rule.top{top:46px}
  .rule.bottom{bottom:46px}

  .cover{left:60px;top:40px;width:290px;height:410px}
  .cover .brand{position:absolute;left:0;right:0;top:175px}

  .outer-spread{left:410px;top:40px;width:730px;height:410px}
  .outer-spread .fold{position:absolute;left:50%;top:0;bottom:0;width:1px;background:rgba(0,0,0,.08)}
  .back-panel{position:absolute;left:0;top:0;width:50%;height:100%;padding:80px 40px}
  .back-panel .brand{margin-bottom:28px}
  .contact-list{list-style:none;display:flex;flex-direction:column;gap:9px}
  .contact-list li{display:flex;align-items:center;gap:9px;font-size:10px;color:var(--gold-deep)}
  .contact-list svg{width:12px;height:12px;flex:none}
  .dot{width:10px;height:10px;border-radius:50%;background:var(--ink);flex:none}
  .front-panel{position:absolute;left:50%;top:0;width:50%;height:100%}
  .front-panel .brand{position:absolute;left:0;right:0;top:175px}

  /* Centre band */
  .showcase{position:absolute;left:0;top:480px;width:1200px;height:320px;background:var(--dark);display:flex;align-items:center;justify-content:center}
  .showcase .brand{gap:18px}
  .showcase .brand-mark{width:34px;height:34px}
  .showcase .brand-name{font-size:58px;letter-spacing:9px}
  .showcase .brand-sub{font-size:22px;letter-spacing:8px}

  /* Inside spreads */
  .spread{position:absolute;top:840px;width:360px;height:270px;display:flex;box-shadow:0 6px 18px rgba(0,0,0,.12)}
  .spread-1{left:30px}.spread-2{left:420px}.spread-3{left:810px}
  .page{position:relative;width:50%;height:100%;padding:12px 12px 20px;background:linear-gradient(100deg,var(--gold-panel-dark),var(--gold-panel));color:var(--text);font-size:5.6px;line-height:1.4}
  .page + .page{background:linear-gradient(100deg,var(--gold-panel),var(--gold-panel-dark) 160%)}
  .page .brand{margin-bottom:7px}
  .page h3{font-size:6px;font-weight:700;margin-top:5px;color:var(--ink)}
  .page h2{font-size:6px;font-weight:700;background:var(--paper);color:var(--ink);padding:1px 3px;margin-bottom:4px;text-transform:uppercase;letter-spacing:.4px}
  .page p{margin-top:1px}
  .page .alert{color:var(--alert);font-weight:700;background:rgba(255,255,255,.35);padding:2px 3px;margin-top:5px}
  .page .url{position:absolute;left:0;right:0;bottom:7px;text-align:center;font-size:5px;opacity:.7}
  .page .mini-list{list-style:none;margin-top:6px;display:flex;flex-direction:column;gap:3px}
  .page .mini-list li{display:flex;align-items:center;gap:4px}
  .page .mini-list i{width:5px;height:5px;background:var(--ink);display:block}
  .notes-title{text-align:center;font-style:italic;font-size:7px;margin-bottom:6px}
  .note-lines{display:flex;flex-direction:column;gap:11px}
  .note-lines span{display:block;height:1px;background:rgba(74,61,32,.25)}
</style>
</head>
<body>

  <!-- Front cover -->
  <section class="sheet cover" aria-label="Front cover">
    <div class="band top"></div><div class="rule top"></div>
    <div class="brand"><span class="brand-mark"></span><span class="brand-name">ELENA MARLOW</span><span class="brand-sub">HAIR EXTENSIONS</span></div>
    <div class="rule bottom"></div><div class="band bottom"></div>
  </section>

  <!-- Outer spread: back panel + front panel -->
  <section class="sheet outer-spread" aria-label="Outer spread">
    <div class="band top"></div><div class="rule top"></div>
    <div class="back-panel">
      <div class="brand small"><span class="brand-mark"></span><span class="brand-name">ELENA MARLOW</span><span class="brand-sub">HAIR EXTENSIONS</span></div>
      <ul class="contact-list">
        <li><span class="dot"></span>elena-marlow-hair-extensions</li>
        <li><span class="dot"></span>elenamarlowhair</li>
        <li><svg viewBox="0 0 12 12"><rect x="1" y="2.5" width="10" height="7" fill="none" stroke="#1e1e1e" stroke-width="1"/><path d="M1 2.5l5 4 5-4" fill="none" stroke="#1e1e1e" stroke-width="1"/></svg>hello@elenamarlow.com</li>
        <li><svg viewBox="0 0 12 12"><path d="M3 1.5l2 2-1 1.5c.6 1.3 1.7 2.4 3 3l1.5-1 2 2-1.2 1.5C5.5 10.5 1.5 6.5 1.5 2.7z" fill="#1e1e1e"/></svg>+61 400 000 123</li>
      </ul>
    </div>
    <div class="fold"></div>
    <div class="front-panel">
      <div class="brand"><span class="brand-mark"></span><span class="brand-name">ELENA MARLOW</span><span class="brand-sub">HAIR EXTENSIONS</span></div>
    </div>
    <div class="rule bottom"></div><div class="band bottom"></div>
  </section>

  <!-- Brand showcase band -->
  <section class="showcase" aria-label="Brand">
    <div class="brand"><span class="brand-mark"></span><span class="brand-name">ELENA MARLOW</span><span class="brand-sub">HAIR EXTENSIONS</span></div>
  </section>

  <!-- Inside spread 1 -->
  <section class="spread spread-1" aria-label="Aftercare guidelines">
    <div class="page">
      <div class="brand small"><span class="brand-mark"></span><span class="brand-name">ELENA MARLOW</span></div>
      <h2>Aftercare and Maintenance Guidelines</h2>
      <h3>General</h3>
      <p>Treat your extensions gently and they will stay soft, smooth and natural for months to come.</p>
      <h3>Brushing</h3>
      <p>Use a soft bristle brush daily, starting at the ends and working slowly up to the roots.</p>
      <h3>Washing</h3>
      <p>Wash no more than twice a week with a mild shampoo, keeping the hair straight while rinsing.</p>
      <p class="alert">Avoid products that contain sulphates or alcohol.</p>
      <span class="url">www.elenamarlow.com</span>
    </div>
    <div class="page">
      <div class="brand small"><span class="brand-mark"></span><span class="brand-name">ELENA MARLOW</span></div>
      <h3>After you washed the hair</h3>
      <p>Apply conditioner from mid lengths to ends only. Pat dry with a towel and never rub.</p>
      <h3>At night</h3>
      <p>Tie hair in a loose braid before sleeping to prevent tangles.</p>
      <h3>Styling the hair</h3>
      <p>Always use a heat protection spray before styling.</p>
      <p class="alert">Important: do not use styling tools that exceed 180 degrees.</p>
      <span class="url">www.elenamarlow.com</span>
    </div>
  </section>

  <!-- Inside spread 2 -->
  <section class="spread spread-2" aria-label="Activities and styling">
    <div class="page">
      <div class="brand small"><span class="brand-mark"></span><span class="brand-name">ELENA MARLOW</span></div>
      <h3>Sports and other activities</h3>
      <p>Tie hair back during exercise and rinse out sweat soon after training.</p>
      <h3>Swimming</h3>
      <p>Wear a cap in pools and the sea, and rinse hair with fresh water straight after.</p>
      <h3>Sunbathing</h3>
      <p>Cover your hair with a hat to protect colour from the sun.</p>
      <span class="url">www.elenamarlow.com</span>
    </div>
    <div class="page">
      <div class="brand small"><span class="brand-mark"></span><span class="brand-name">ELENA MARLOW</span></div>
      <h3>General daily styling guide</h3>
      <p>Brush gently from ends to roots each morning and evening.</p>
      <p class="alert">Important: keep heat below 180 degrees.</p>
      <h3>Chemical treatments</h3>
      <p>Please ask your stylist before any colouring, perming or toning.</p>
      <h3>Colouring your extensions</h3>
      <p>Extensions can be darkened but never lightened. Strand test first.</p>
      <span class="url">www.elenamarlow.com</span>
    </div>
  </section>

  <!-- Inside spread 3 -->
  <section class="spread spread-3" aria-label="Contact and notes">
    <div class="page">
      <div class="brand small"><span class="brand-mark"></span><span class="brand-name">ELENA MARLOW</span></div>
      <p>Thank you for choosing us. With the right care your extensions will look beautiful every day.</p>
      <h3>For more information or questions please visit the website</h3>
      <ul class="mini-list">
        <li><i></i>www.elenamarlow.com</li>
        <li><i></i>hello@elenamarlow.com</li>
        <li><i></i>+61 400 000 123</li>
      </ul>
      <h3>Follow us on social media</h3>
      <ul class="mini-list">
        <li><i></i>elena-marlow-hair-extensions</li>
        <li><i></i>elenamarlowhair</li>
      </ul>
      <span class="url">www.elenamarlow.com</span>
    </div>
    <div class="page">
      <div class="brand small"><span class="brand-mark"></span><span class="brand-name">ELENA MARLOW</span></div>
      <div class="notes-title">Notes</div>
      <div class="note-lines"><span></span><span></span><span></span><span></span><span></span><span></span><span></span><span></span><span></span><span></span><span></span><span></span><span></span></div>
      <span class="url">www.elenamarlow.com</span>
    </div>
  </section>

</body>
</html>
```